Business Card Design with new logo

Dorian Pelleway 4172
E 118th St Brennet, IL 62901
Cell: 217-555-0193
pellewayrestoration@mailvane.test

Classic Car Restoration Services Buy Sell Trade Consign

Dorian Pelleway 9698
Cell: 217-555-0193

```html
<!DOCTYPE html>
<html lang="en">
<head>
<meta charset="utf-8">
<title>Pelleway Restoration – Business Cards</title>
<link href="https://fonts.googleapis.com/css2?family=Lato:wght@400;700&display=swap" rel="stylesheet">
<style>
  :root {
    --page: #e4e6e8;
    --card: #0b0b0c;
    --card-soft: #26272a;
    --red: #d8262c;
    --white: #f4f4f4;
    --grey: #bdbdbd;
  }
  * { margin: 0; padding: 0; box-sizing: border-box; }
  html, body { width: 1200px; height: 1200px; overflow: hidden; }
  body {
    background: var(--page);
    font-family: "Lato", sans-serif;
    position: relative;
  }
  .card {
    position: absolute;
    left: 150px;
    width: 900px;
    height: 514px;
    border-radius: 40px;
    overflow: hidden;
    background: var(--card);
    box-shadow: 0 18px 40px rgba(0,0,0,0.25);
  }
  .card--front { top: 50px; }
  .card--back { top: 636px; }
  .card__photo {
    position: absolute; inset: 0;
    background: radial-gradient(ellipse at 65% 45%, var(--card-soft) 0%, #121214 45%, var(--card) 80%);
  }
  .wordmark {
    position: absolute;
    color: var(--white);
    font-weight: 700;
    text-transform: uppercase;
    display: flex;
    align-items: center;
    gap: 18px;
  }
  .wordmark__dot {
    width: 26px; height: 26px; border-radius: 50%;
    background: var(--white);
  }
  .wordmark__lines { line-height: 1.05; }
  .wordmark__name { font-size: 64px; letter-spacing: 3px; display: block; }
  .wordmark__sub { font-size: 22px; letter-spacing: 11px; display: block; margin-top: 6px; }
  .card--front .wordmark { left: 50%; top: 150px; transform: translateX(-50%); }
  .card--back .wordmark { left: 70px; top: 200px; }
  .card--back .wordmark__name { font-size: 54px; }
  .card--back .wordmark__sub { font-size: 18px; letter-spacing: 9px; }

  .services { position: absolute; left: 0; top: 380px; }
  .services__band {
    background: var(--red);
    color: var(--white);
    font-size: 26px;
    letter-spacing: 1px;
    padding: 8px 60px 8px 130px;
    clip-path: polygon(0 0, 94% 0, 100% 100%, 0 100%);
    width: 520px;
  }
  .services__list {
    display: flex; gap: 22px;
    list-style: none;
    margin: 10px 0 0 190px;
    color: var(--grey);
    font-size: 22px;
  }
  .services__list li::before { content: "✓"; color: var(--red); margin-right: 6px; font-weight: 700; }

  .divider {
    position: absolute; left: 480px; top: 120px;
    width: 3px; height: 260px;
    background: linear-gradient(var(--red), transparent);
  }
  .contact {
    position: absolute; left: 510px; top: 135px;
    list-style: none;
    color: var(--white);
    font-size: 24px;
  }
  .contact li { display: flex; align-items: flex-start; gap: 14px; margin-bottom: 22px; line-height: 1.25; }
  .contact svg { flex: none; width: 26px; height: 26px; margin-top: 2px; }
  .contact__email { font-size: 20px; }
</style>
</head>
<body>
  <section class="card card--front">
    <div class="card__photo" role="img" aria-label="Faint dark photo of a classic car interior"></div>
    <div class="wordmark">
      <span class="wordmark__dot"></span>
      <span class="wordmark__lines">
        <span class="wordmark__name">Pelleway</span>
        <span class="wordmark__sub">Restoration LLC</span>
      </span>
    </div>
    <div class="services">
      <div class="services__band">Classic Car Restoration</div>
      <ul class="services__list">
        <li>Buy</li><li>Sell</li><li>Trade</li><li>Consign</li>
      </ul>
    </div>
  </section>

  <section class="card card--back">
    <div class="card__photo" role="img" aria-label="Faint dark photo of a classic car front with headlight and wheel"></div>
    <div class="wordmark">
      <span class="wordmark__dot"></span>
      <span class="wordmark__lines">
        <span class="wordmark__name">Pelleway</span>
        <span class="wordmark__sub">Restoration LLC</span>
      </span>
    </div>
    <div class="divider"></div>
    <ul class="contact">
      <li>
        <svg viewBox="0 0 24 24" fill="none" stroke="#d8262c" stroke-width="2"><path d="M5 3h4l2 5-3 2a11 11 0 0 0 6 6l2-3 5 2v4a2 2 0 0 1-2 2A17 17 0 0 1 3 5a2 2 0 0 1 2-2z"/></svg>
        <span>217-555-0193</span>
      </li>
      <li>
        <svg viewBox="0 0 24 24" fill="none" stroke="#d8262c" stroke-width="2"><rect x="6" y="3" width="12" height="18" rx="6"/><line x1="12" y1="7" x2="12" y2="10"/></svg>
        <span class="contact__email">pellewayrestoration@mailvane.test</span>
      </li>
      <li>
        <svg viewBox="0 0 24 24" fill="none" stroke="#d8262c" stroke-width="2"><path d="M12 22s7-7 7-12a7 7 0 0 0-14 0c0 5 7 12 7 12z"/><circle cx="12" cy="10" r="2.5"/></svg>
        <span>Dorian Pelleway 4172<br>E 118th St Brennet, IL 62901</span>
      </li>
    </ul>
  </section>
</body>
</html>
```